International Legal Service Company needs Letterhead Design

Put my new Logo into Letterhead Design, using updated telephone number, e-mail address and website. Current letterhead and updated information which i want you to include my new letterhead attached herewith. Of course, my new Logo attached herein. Also, you can use slogan "Complete Legal Support Services For International Enterprises"

It Company

```html
<!DOCTYPE html>
<html lang="en">
<head>
<meta charset="utf-8">
<title>Meridian Counsel Partners Inc – Letterhead</title>
<link rel="stylesheet" href="https://fonts.googleapis.com/css2?family=Open+Sans:wght@400;600&display=swap">
<style>
  :root {
    --brand-blue: #0b3d7e;
    --rule-blue: #1d4f9a;
    --band-dark: #083670;
    --band-light: #6ea6dc;
    --text-dark: #2a2a2a;
    --paper: #ffffff;
    --backdrop: #ffffff;
  }
  html, body {
    margin: 0;
    padding: 0;
    width: 929px;
    height: 1200px;
    overflow: hidden;
    background: var(--backdrop);
    font-family: "Open Sans", Arial, sans-serif;
  }
  .letterhead {
    position: absolute;
    left: 58px;
    top: 74px;
    width: 815px;
    height: 1056px;
    background: var(--paper);
  }
  .brand {
    position: absolute;
    left: 27px;
    top: 28px;
    display: flex;
    align-items: center;
    gap: 16px;
  }
  .brand-mark {
    width: 104px;
    height: 104px;
    border-radius: 50%;
    background: var(--brand-blue);
    flex: none;
  }
  .brand-name {
    margin: 0;
    color: var(--brand-blue);
    font-weight: 600;
    font-size: 25px;
    line-height: 30px;
  }
  .contact {
    position: absolute;
    right: 32px;
    top: 36px;
    margin: 0;
    text-align: right;
    font-style: normal;
    font-size: 10.5px;
    line-height: 14.6px;
    color: var(--text-dark);
  }
  .header-rule {
    position: absolute;
    left: 12px;
    top: 155px;
    width: 791px;
    height: 2px;
    background: var(--rule-blue);
  }
  .slogan-band {
    position: absolute;
    left: 12px;
    top: 1010px;
    width: 791px;
    height: 34px;
    background: linear-gradient(90deg, var(--band-dark) 0%, var(--band-light) 50%, var(--band-dark) 100%);
    color: #fff;
    font-size: 15px;
    line-height: 34px;
    text-align: center;
  }
</style>
</head>
<body>
  <main class="letterhead">
    <header>
      <div class="brand">
        <span class="brand-mark" aria-hidden="true"></span>
        <p class="brand-name">Meridian Counsel<br>Partners Inc</p>
      </div>
      <address class="contact">
        4180 Harbor Point Drive<br>
        Suite 500<br>
        Lakeside, MD 20990<br>
        Tel: 240-555-0148<br>
        Fax: 240-555-0192<br>
        E-Mail: info@meridiancounsel.com<br>
        Website: http://meridiancounsel.com
      </address>
      <div class="header-rule"></div>
    </header>
    <footer class="slogan-band">Complete Legal Support Services For International Enterprises</footer>
  </main>
</body>
</html>
```